Travinex - You are the Boss!

Travinex is a new Silicon Valley company, of the pelim founders from Berlin, which provides a "Shared Pioneer Circle". This platform allows the crowd to support startups with money, experts and fame. Our Vision is, that everyone should become an entrepreneur.

Pls find all brief details in the attached document
Updates

Would be nice to have a list of more social services I'm available on, like a list of pictograms of all my services:

Find me on: vooka, bramlet+, qrt, fenwix, moodrail, zupp, hvoxa, etc...

pls make sure to use the right font:
http://www.typemarlow.com/fonts/Velquin

Target Market(s)

Main target market is those already involved in the startup industry, by fundraising, investing, advising, cofounding and working. Travinex brings a totaly new transparency and collaborative way of starting companies to that business.

· Entrepreneurs (looking for funding, team and community)
· Investors (looking for hot investments and )
· Experts (workers looking for startups they can work for equity)
· Incubators & Business Schools (looking for tools to advise startups)

Industry/Entity Type

It Company

Requirements
Must have
• Pls find all brief details in the attached document
Nice to have

```html
<!DOCTYPE html>
<html lang="en">
<head>
<meta charset="utf-8">
<title>Travinex – Business Card</title>
<link rel="stylesheet" href="https://fonts.googleapis.com/css2?family=Orbitron:wght@500;700&family=Exo+2:ital,wght@0,500;0,600;1,400&display=swap">
<style>
  :root {
    --orange: #f2843a;
    --charcoal: #3a3a3a;
    --ink: #333333;
    --teal: #2a9faa;
    --paper: #ffffff;
    --canvas: #ffffff;
    --rule-teal: #3aa6ad;
  }
  * { margin: 0; padding: 0; box-sizing: border-box; }
  html, body {
    width: 1200px; height: 900px; overflow: hidden;
    background: var(--canvas);
  }
  .stage { position: relative; width: 1200px; height: 900px; }

  .card {
    position: absolute; top: 194px; width: 288px; height: 510px;
    background: var(--paper);
    box-shadow: 0 2px 8px rgba(0,0,0,0.35);
    overflow: hidden;
    font-family: "Exo 2", sans-serif;
  }
  .card--front { left: 256px; }
  .card--back  { left: 644px; }

  /* Front */
  .front__brand {
    position: absolute; left: 0; top: 0; width: 100%; height: 164px;
    display: flex; flex-direction: column; align-items: center; justify-content: flex-end;
    padding-bottom: 14px;
  }
  .brand {
    display: flex; align-items: center; gap: 12px; margin-bottom: 10px;
  }
  .brand__dot { width: 34px; height: 34px; border-radius: 50%; background: var(--orange); }
  .brand__name {
    font-family: "Orbitron", sans-serif; font-weight: 700; font-size: 30px;
    color: var(--ink); letter-spacing: 1px;
  }
  .tagline { font-style: italic; font-weight: 400; font-size: 17px; color: var(--ink); }
  .front__divider {
    position: absolute; left: 0; top: 164px; width: 100%; height: 4px; background: var(--orange);
  }
  .front__panel {
    position: absolute; left: 0; top: 168px; width: 100%; bottom: 0;
    background: var(--charcoal); color: #ffffff; text-align: center;
  }
  .person__name {
    position: absolute; top: 26px; width: 100%;
    font-family: "Orbitron", sans-serif; font-weight: 500; font-size: 22px; letter-spacing: 0.5px;
  }
  .person__title {
    position: absolute; top: 54px; width: 100%;
    font-style: italic; font-size: 19px;
  }
  .rule {
    position: absolute; left: 64px; width: 160px; height: 2px; background: var(--rule-teal);
  }
  .rule--upper { top: 102px; }
  .rule--lower { top: 230px; }
  .contact {
    position: absolute; top: 128px; width: 100%; list-style: none;
    font-family: "Orbitron", sans-serif; font-weight: 500; font-size: 15px; line-height: 22px;
  }
  .contact li:first-child { font-size: 17px; }
  .social {
    position: absolute; top: 258px; width: 100%; list-style: none;
    font-family: "Orbitron", sans-serif; font-weight: 500; font-size: 13px; line-height: 22px;
  }

  /* Back */
  .back__heading {
    position: absolute; top: 44px; width: 100%; text-align: center;
    font-family: "Orbitron", sans-serif; font-weight: 700; font-size: 19px; color: var(--ink);
  }
  .back__rule {
    position: absolute; top: 80px; left: 0; width: 100%; height: 2px; background: var(--rule-teal);
  }
  .interests {
    position: absolute; top: 94px; left: 40px; right: 16px; list-style: none;
    font-family: "Orbitron", sans-serif; font-weight: 500; font-size: 19px; line-height: 25px;
    color: var(--ink);
  }
  .interests li { padding-left: 16px; text-indent: -16px; margin-bottom: 18px; }
  .interests li .indent { padding-left: 16px; }
  .back__brand {
    position: absolute; top: 332px; width: 100%;
    display: flex; align-items: center; justify-content: center; gap: 14px;
  }
  .back__brand .brand__dot { width: 48px; height: 48px; }
  .back__brand .brand__name { font-size: 34px; color: var(--orange); }
  .join {
    position: absolute; top: 424px; width: 100%; text-align: center;
    font-family: "Exo 2", sans-serif; font-weight: 600; font-size: 19px; line-height: 26px;
    color: var(--teal);
  }
</style>
</head>
<body>
<main class="stage">

  <section class="card card--front" aria-label="Business card front">
    <header class="front__brand">
      <div class="brand">
        <span class="brand__dot"></span>
        <span class="brand__name">Travinex</span>
      </div>
      <p class="tagline">You are the boss!</p>
    </header>
    <div class="front__divider"></div>
    <div class="front__panel">
      <h1 class="person__name">Jonas Keller</h1>
      <p class="person__title">Founder and CEO</p>
      <div class="rule rule--upper"></div>
      <ul class="contact">
        <li>650-480-2917</li>
        <li>hi@travinex.com</li>
        <li>www.travinex.com</li>
      </ul>
      <div class="rule rule--lower"></div>
      <ul class="social">
        <li>chirpline.com/jonaskeller</li>
        <li>friendhub.com/jonaskeller</li>
        <li>linkpro.com/in/jonaskeller</li>
      </ul>
    </div>
  </section>

  <section class="card card--back" aria-label="Business card back">
    <h2 class="back__heading">Are you interested in:</h2>
    <div class="back__rule"></div>
    <ul class="interests">
      <li>- Starting your own<br><span class="indent">business?</span></li>
      <li>- Investing in hot<br><span class="indent">startups?</span></li>
      <li>- Working for the<br><span class="indent">next “Friendhub”?</span></li>
    </ul>
    <div class="back__brand">
      <span class="brand__dot"></span>
      <span class="brand__name">Travinex</span>
    </div>
    <p class="join">Join us on<br>friendhub.com/Travinex</p>
  </section>

</main>
</body>
</html>
```